Professional Report Cover

We need a cover for CFO report (the document is about 20 pages, in case you decide to provide 3D mockup). The design must be professional. The main color has to be #299FC0, which can be incorporated with white, #375172, and #E3E7EE. See attached for content and logo.

```html
<!DOCTYPE html>
<html lang="en">
<head>
<meta charset="utf-8">
<title>The CFO Insight — Report Cover</title>
<link rel="stylesheet" href="https://fonts.googleapis.com/css2?family=Bebas+Neue&family=Montserrat:wght@500;700;800&display=swap">
<style>
  :root {
    --navy: #375172;
    --teal: #299FC0;
    --mist: #E3E7EE;
    --white: #FFFFFF;
  }
  html, body {
    margin: 0;
    padding: 0;
    width: 800px;
    height: 1200px;
    overflow: hidden;
    background: var(--navy);
  }
  .cover {
    position: relative;
    width: 800px;
    height: 1200px;
    background: var(--navy);
    overflow: hidden;
  }
  .title-word {
    position: absolute;
    margin: 0;
    font-family: "Bebas Neue", "Oswald", sans-serif;
    font-weight: 400;
    line-height: 1;
    white-space: nowrap;
  }
  .title-the {
    left: 66px;
    top: 175px;
    font-size: 180px;
    color: var(--mist);
  }
  .title-cfo {
    left: 320px;
    top: 26px;
    font-size: 378px;
    color: var(--teal);
    letter-spacing: 4px;
  }
  .title-insight {
    left: 76px;
    top: 357px;
    font-size: 282px;
    color: var(--teal);
    letter-spacing: 1px;
  }
  .highlights {
    position: absolute;
    left: 66px;
    top: 657px;
    width: 700px;
    margin: 0;
    padding: 0;
    list-style: none;
  }
  .highlight {
    position: relative;
    padding-left: 47px;
    margin-bottom: 34px;
    font-family: "Montserrat", sans-serif;
    font-size: 18.5px;
    line-height: 26px;
    letter-spacing: 2.6px;
    text-transform: uppercase;
    font-weight: 500;
    color: var(--mist);
  }
  .highlight::before {
    content: "";
    position: absolute;
    left: 0;
    top: 3px;
    bottom: 3px;
    width: 4px;
    background: var(--mist);
  }
  .highlight--accent {
    font-weight: 800;
    color: var(--teal);
  }
  .highlight--accent::before { background: var(--teal); }
  .accent { color: var(--teal); font-weight: 800; }
  .brand-tile {
    position: absolute;
    left: 305px;
    top: 1040px;
    width: 192px;
    height: 160px;
    background: var(--teal);
    display: flex;
    flex-direction: column;
    align-items: center;
    justify-content: center;
    font-family: "Montserrat", sans-serif;
    font-weight: 700;
    color: var(--white);
    text-align: center;
  }
  .brand-name {
    font-size: 22px;
    letter-spacing: 2px;
    line-height: 1.15;
    margin: 0;
  }
  .brand-name small {
    display: block;
    font-size: 10px;
    letter-spacing: 1px;
    margin-top: 4px;
  }
  .brand-parent {
    margin: 18px 0 0;
    font-size: 7.5px;
    letter-spacing: 1px;
  }
</style>
</head>
<body>
  <main class="cover">
    <h1 class="report-title">
      <span class="title-word title-the">THE</span>
      <span class="title-word title-cfo">CFO</span>
      <span class="title-word title-insight">INSIGHT</span>
    </h1>

    <ul class="highlights">
      <li class="highlight highlight--accent">Insights into external, enterprise and departmental challenges.</li>
      <li class="highlight">Best practices and strategies to slove these challendes, <span class="accent">with a focus</span> on innovation, sexuring competitive advantage and opportunities for growth.</li>
      <li class="highlight highlight--accent">Finance industry trznds in the 2020s.</li>
      <li class="highlight">The leading role of CFOs in business transformation.</li>
    </ul>

    <footer class="brand-tile">
      <p class="brand-name">ORVANE<small>DOCUMENT SERVICES</small></p>
      <p class="brand-parent">A MERIDIAN GROUP COMPANY</p>
    </footer>
  </main>
</body>
</html>
```